Computer business needs new look.

KELD Computers has been selling and repairing, servicing computers in northern NSW for 20 years and has now branched out into Surveillance/ CCTV systems Alarm systems and just about anything technical.
We have also changed our area of operation from just the northern rivers to include all of outback New South Wales and Queensland.
We have changed our name slightly to K.E.L.D Sundown Technical Services.I will include my old business card.The Logo can stay or go i am open to all designs.
Updates

facebook page for info https://www.examplebook.test/pages/KELD-Computers/482019375610283?fref=ts The top half of the business card i uploaded looks pink ! it should be white

I should have mentioned this before. My new look cards will become the look of the business. ie: advertising, vehicle sign-writing etc: The look that i think im after is more to large business/corporate look not "WALLY THE FIXER " Probably the main focus is the fact that we service the small towns in outback Australia. " Billabong Barney " Not just the big city's Please feel free to through any thing at me and any questions please ask.

I have uploaded a picture that i would like the back of the card to look like. Please have a look and see what you can do.

Reason: I am hoping to get some original designs that i like. So far i have just 1 that i like..there must be more ideas out there.

Target Market(s)

Small to medium business

Industry/Entity Type

Business

Contact Information for Business Card

K.E.L.D Sundown Technical Services
Owen Pelkie
1300621745 0457 318206

Requirements
Nice to have
• Back of card to have a list of services
Computer sales
Computer Repairs & Virus removal
Wireless Hotspots
CCTV Installation and repair
Network Design and setup
Troubleshooting

```html
<!DOCTYPE html>
<html lang="en">
<head>
<meta charset="utf-8">
<title>K.E.L.D Sundown Technical Services — Business Card</title>
<link rel="stylesheet" href="https://fonts.googleapis.com/css2?family=Roboto:wght@400;500&display=swap">
<style>
  :root {
    --page-bg: #e9e7e3;
    --card-white: #ffffff;
    --card-shade: #eceeef;
    --name-ink: #2f3a46;
    --band-blue: #1f76a6;
    --band-edge: #17628c;
    --icon-indigo: #3d4fa8;
    --text-grey: #5a6470;
    --shadow: rgba(40, 35, 25, 0.28);
  }
  * { box-sizing: border-box; margin: 0; padding: 0; }
  html, body {
    width: 1057px;
    height: 1200px;
    overflow: hidden;
    background: var(--page-bg);
    font-family: "Roboto", Arial, sans-serif;
  }
  .sheet {
    position: relative;
    width: 1057px;
    height: 1200px;
  }
  .card {
    position: absolute;
    left: 118px;
    width: 820px;
    height: 469px;
    background: linear-gradient(135deg, var(--card-white) 55%, var(--card-shade) 100%);
    box-shadow: 0 14px 34px var(--shadow);
    overflow: hidden;
  }
  .card--front { top: 70px; }
  .card--back { top: 640px; }

  .business-name {
    position: absolute;
    color: var(--name-ink);
    font-weight: 500;
    line-height: 1.2;
    white-space: nowrap;
  }
  .card--front .business-name {
    top: 50%;
    left: 50%;
    transform: translate(-50%, -50%);
    font-size: 34px;
  }
  .card--back .business-name {
    top: 160px;
    left: 52px;
    font-size: 22px;
  }

  .title-band {
    position: absolute;
    top: 46px;
    right: 0;
    width: 330px;
    height: 104px;
    background: var(--band-blue);
    border-left: 8px solid var(--band-edge);
    color: #fff;
    display: flex;
    flex-direction: column;
    justify-content: center;
    padding-left: 30px;
  }
  .title-band__name {
    font-size: 28px;
    font-weight: 500;
    letter-spacing: 1px;
    white-space: nowrap;
  }
  .title-band__role {
    font-size: 15px;
    letter-spacing: 2px;
    margin-top: 6px;
  }

  .contact-list {
    position: absolute;
    left: 140px;
    top: 262px;
    list-style: none;
  }
  .contact-list__item {
    display: flex;
    align-items: center;
    gap: 14px;
    height: 32px;
    font-size: 15px;
    color: var(--text-grey);
  }
  .contact-list__icon {
    width: 22px;
    height: 22px;
    flex: none;
  }
</style>
</head>
<body>
<main class="sheet">

  <section class="card card--front" aria-label="Card front">
    <p class="business-name">K.E.L.D Sundown Technical Services</p>
  </section>

  <section class="card card--back" aria-label="Card back">
    <div class="title-band">
      <span class="title-band__name">ROSS HALVERTON</span>
      <span class="title-band__role">FOUNDER</span>
    </div>

    <p class="business-name">K.E.L.D Sundown Technical Services</p>

    <ul class="contact-list">
      <li class="contact-list__item">
        <svg class="contact-list__icon" viewBox="0 0 22 22" aria-hidden="true">
          <rect width="22" height="22" fill="var(--icon-indigo)"/>
          <path d="M7 5h3l1 3-2 1a8 8 0 0 0 4 4l1-2 3 1v3c0 1-1 1-1 1A11 11 0 0 1 6 6s0-1 1-1z" fill="#fff"/>
        </svg>
        <span>010 555 0142</span>
      </li>
      <li class="contact-list__item">
        <svg class="contact-list__icon" viewBox="0 0 22 22" aria-hidden="true">
          <rect width="22" height="22" fill="var(--icon-indigo)"/>
          <rect x="7" y="4" width="8" height="14" rx="1.5" fill="none" stroke="#fff" stroke-width="1.6"/>
          <circle cx="11" cy="15.5" r="0.9" fill="#fff"/>
        </svg>
        <span>010 555 0142</span>
      </li>
      <li class="contact-list__item">
        <svg class="contact-list__icon" viewBox="0 0 22 22" aria-hidden="true">
          <rect width="22" height="22" fill="var(--icon-indigo)"/>
          <circle cx="11" cy="11" r="6" fill="none" stroke="#fff" stroke-width="1.4"/>
          <path d="M5 11h12M11 5c-3 3.5-3 8.5 0 12M11 5c3 3.5 3 8.5 0 12" fill="none" stroke="#fff" stroke-width="1.2"/>
        </svg>
        <span>www.sundowntech.example</span>
      </li>
      <li class="contact-list__item">
        <svg class="contact-list__icon" viewBox="0 0 22 22" aria-hidden="true">
          <rect width="22" height="22" fill="var(--icon-indigo)"/>
          <rect x="5" y="7" width="12" height="9" fill="none" stroke="#fff" stroke-width="1.4"/>
          <path d="M5 7l6 5 6-5" fill="none" stroke="#fff" stroke-width="1.4"/>
        </svg>
        <span>hello@sundowntech.example</span>
      </li>
      <li class="contact-list__item">
        <svg class="contact-list__icon" viewBox="0 0 22 22" aria-hidden="true">
          <rect width="22" height="22" fill="var(--icon-indigo)"/>
          <path d="M11 18s-5-5.5-5-9a5 5 0 0 1 10 0c0 3.5-5 9-5 9z" fill="#fff"/>
          <circle cx="11" cy="9" r="1.8" fill="var(--icon-indigo)"/>
        </svg>
        <span>14 Red Gum Lane, Outback NSW</span>
      </li>
    </ul>
  </section>

</main>
</body>
</html>
```